Album Jacket for young indie musicians in AFRICA #2 Baraka, Tumaini And Neema (Grace, Hope And Blessing)

We are ZEV SOUND (zev-sound.example), a music label for young African musicians living in a slum. I would like to ask you to design our new album's cover jacket. The title is Baraka, Tumaini And Neema (it means "Grace, Hope And Blessing" in Swahili. I entrust you whether you use English words in the design or not.), musician name is Jabari Okoth. Add our label logo (we have various versions and can provide). I attached Jabari Okoth's photo also. Please listen to the music of the album on Soundcloud. https://tunecove.example/tags/jabariokoth

Target Market(s)

International. not only African music funs.

Requirements
Must have
• Title, Musician's name, ZEV SOUND Logo
• In order to upload to iTunes, I require the final that the following conditions are met.
• 1400 x 1400 pixels
• JPG file type
• 72 - 300dpi (300dpi is the best)
• Less than 25mb
• RGB color scheme (not CMYK)
Nice to have
• His music is something bright and little funny. Please express the tone of music in the design.
Should not have
• African traditional image

```html
<!DOCTYPE html>
<html lang="en">
<head>
<meta charset="utf-8">
<title>Jabari Okoth – Baraka, Tumaini &amp; Neema</title>
<link rel="stylesheet" href="https://fonts.googleapis.com/css2?family=Open+Sans:wght@300&display=swap">
<style>
  :root {
    --ink: #ffffff;
    --warm: #7a2414;
    --moss: #2a6a22;
    --emerald: #22b04a;
    --teal: #1fa89a;
    --violet: #5a1c78;
    --indigo: #3030a8;
  }
  html, body {
    margin: 0;
    padding: 0;
    width: 1200px;
    height: 1200px;
    overflow: hidden;
    background: #000;
  }
  .cover {
    position: relative;
    width: 1200px;
    height: 1200px;
    overflow: hidden;
  }
  .cover__art,
  .cover__type {
    position: absolute;
    inset: 0;
  }
  .cover__type text {
    fill: var(--ink);
    font-family: "Open Sans", "Segoe UI", sans-serif;
    font-weight: 300;
    text-anchor: middle;
  }
  .artist-name { font-size: 112px; letter-spacing: -2px; }
  .album-title { font-size: 224px; letter-spacing: -5px; }
  .label-name { font-size: 30px; letter-spacing: 4px; }
  .label-dot { fill: none; stroke: var(--ink); stroke-width: 2; }
</style>
</head>
<body>
<main class="cover">
  <svg class="cover__art" role="img" aria-label="Bright fluid marbled paint swirls in red-brown, vivid green, teal and violet-blue" width="1200" height="1200" viewBox="0 0 1200 1200">
    <defs>
      <linearGradient id="marble-base" x1="0" y1="0" x2="1" y2="0.3">
        <stop offset="0" stop-color="var(--warm)"/>
        <stop offset="0.38" stop-color="var(--moss)"/>
        <stop offset="0.72" stop-color="var(--violet)"/>
        <stop offset="1" stop-color="var(--indigo)"/>
      </linearGradient>
      <radialGradient id="glow-green" cx="0.5" cy="0.7" r="0.42">
        <stop offset="0" stop-color="var(--emerald)" stop-opacity="0.9"/>
        <stop offset="1" stop-color="var(--emerald)" stop-opacity="0"/>
      </radialGradient>
      <radialGradient id="glow-teal" cx="0.3" cy="0.2" r="0.3">
        <stop offset="0" stop-color="var(--teal)" stop-opacity="0.55"/>
        <stop offset="1" stop-color="var(--teal)" stop-opacity="0"/>
      </radialGradient>
      <radialGradient id="glow-blue" cx="0.88" cy="0.55" r="0.3">
        <stop offset="0" stop-color="#3a5ad8" stop-opacity="0.7"/>
        <stop offset="1" stop-color="#3a5ad8" stop-opacity="0"/>
      </radialGradient>
      <radialGradient id="glow-red" cx="0" cy="0.85" r="0.35">
        <stop offset="0" stop-color="#a83018" stop-opacity="0.6"/>
        <stop offset="1" stop-color="#a83018" stop-opacity="0"/>
      </radialGradient>
    </defs>
    <rect width="1200" height="1200" fill="url(#marble-base)"/>
    <rect width="1200" height="1200" fill="url(#glow-green)"/>
    <rect width="1200" height="1200" fill="url(#glow-teal)"/>
    <rect width="1200" height="1200" fill="url(#glow-blue)"/>
    <rect width="1200" height="1200" fill="url(#glow-red)"/>
  </svg>

  <svg class="cover__type" width="1200" height="1200" viewBox="0 0 1200 1200">
    <text class="artist-name" x="600" y="123">JABARI OKOTH</text>
    <text class="album-title" x="600" y="456">BARAKA</text>
    <text class="album-title" x="600" y="713">TUMAINI</text>
    <text class="album-title" x="600" y="971">&amp; NEEMA</text>
    <g class="label-mark">
      <circle class="label-dot" cx="518" cy="1139" r="11"/>
      <text class="label-name" x="614" y="1150">ZEV SOUND</text>
    </g>
  </svg>
</main>
</body>
</html>
```